Small and passionate motorcycle workshop requires a business card that kicks butt!

I'm Darren, I'm passionate about my motorcycles, I'm passionate about my desert racing and I'm a passionate motorcycle technician, that's why I started my own motorcycle workshop: 'Rivo Tanza'.
I started my workshop in my dining room and it’s eventually moved into a newly renovated shed that my Grandpa built with his own two hands in the early 1960's. To the customer the shed looks like a farm shed on my property, however the inside is ready for open heart surgery on their "Baby" which could be a late model sports bike, a highway cruiser, an old four-wheeler or an off road desert racing weapon!
This business is my own, I've built it from my dining room floor and I'm deeply passionate about it.
I need a professional business card and logo which looks like a heart and soul is intermingled through it because that is how my business is run. Rivo Tanza may have started from my dining room but it has always been professionally run and I have always put my passion into the bikes I've worked on.

-The text only logo needs to be comprised of 'Rivo Tanza'
-The business card will be double sided

And I do realise it will be a hard task to make something look professional and personal at the same time...however there are some very talented people in this world and I can’t wait to see what you create!

I've added some logo/designs that I'm fond of.

Industry/Entity Type

Racing

Requirements
Must have
• My name - Darren Pulkett
My Qualification - Qualified Motorcycle Technician
Ph - 0471 582 930
Email - rivotanza@quillmail.example
Address - 17 Bellbrook Lane, Larkvale, QLD
ABN - 61 804 392 117 (plesase include the 'ABN' part
Needs to include these dot points:
-Servicing
-Repairs
-All makes/models
-Weekends by appt.
-Pick-up/delivery available
Nice to have
• I like the idea of calling myself a "Qualified and Passionate Motorcycle Technician". If the card does not come across that it’s a passionate business I'd like this line to be used on the card near my name.

One idea I like would include having the text only logo on the front being quite bold and contrasted to the background, then having my name and number smaller underneath somewhere. I'm very open to whatever comes my way so I'm look forward to seeing some sweet ideas!

```html
<!DOCTYPE html>
<html lang="en">
<head>
<meta charset="utf-8">
<title>Rivo Tanza — Business Card</title>
<link rel="stylesheet" href="https://fonts.googleapis.com/css2?family=Didact+Gothic&display=swap">
<style>
  :root {
    --stage: #cfcfd1;
    --card-white: #ffffff;
    --panel-top: #434345;
    --panel-bottom: #2b2b2d;
    --accent-blue: #2f56c6;
    --logo-blue: #2f56c6;
    --text-light: #f4f4f4;
    --font-main: "Didact Gothic", "Century Gothic", sans-serif;
  }
  * { box-sizing: border-box; margin: 0; padding: 0; }
  html, body {
    width: 1200px; height: 800px; overflow: hidden;
    background: var(--stage);
    font-family: var(--font-main);
  }
  .stage {
    width: 1200px; height: 800px;
    display: flex; flex-direction: column; align-items: center; justify-content: center;
    gap: 40px;
  }
  .card {
    position: relative;
    width: 630px; height: 350px;
    background: var(--card-white);
    box-shadow: 0 6px 18px rgba(0,0,0,0.18);
    overflow: hidden;
  }
  .card-panel { position: absolute; inset: 0; width: 630px; height: 350px; }

  .logo {
    position: absolute; right: 42px; top: 40px;
    color: var(--logo-blue);
    font-family: var(--font-main);
    font-weight: 400;
    font-size: 52px; line-height: 0.95; letter-spacing: 1px;
    text-transform: uppercase; text-align: left;
  }
  .card-back .logo { top: 26px; }

  /* Front: contact */
  .owner-name {
    position: absolute; left: 66px; top: 168px;
    color: var(--text-light);
    font-weight: 400;
    font-size: 26px; letter-spacing: 2px;
  }
  .owner-title {
    position: absolute; left: 68px; top: 207px;
    color: var(--accent-blue);
    font-size: 15px; letter-spacing: 1.2px;
  }
  .contact-list {
    position: absolute; left: 40px; top: 244px;
    display: grid; grid-template-columns: 90px auto; row-gap: 4px;
    font-size: 16px; letter-spacing: 1px;
  }
  .contact-label { color: var(--accent-blue); }
  .contact-value { color: var(--text-light); }

  /* Back: services */
  .service-list {
    position: absolute; left: 78px; top: 158px;
    list-style: none;
    color: var(--text-light);
    font-size: 18px; letter-spacing: 1.5px;
  }
  .service-item { display: flex; align-items: center; gap: 14px; margin-bottom: 9px; }
  .bullet { width: 12px; height: 10px; flex: none; }
</style>
</head>
<body>
<main class="stage">

  <section class="card card-front" aria-label="Business card front">
    <svg class="card-panel" viewBox="0 0 630 350" aria-hidden="true">
      <defs>
        <linearGradient id="panelShade" x1="0" y1="0" x2="0.4" y2="1">
          <stop offset="0" stop-color="#434345"/>
          <stop offset="1" stop-color="#2b2b2d"/>
        </linearGradient>
      </defs>
      <path d="M0 208 H38 Q50 208 52 196 L54 168 Q56 156 68 156 H360 Q372 156 374 168 L376 184 Q378 196 390 196 H630 V350 H0 Z" fill="url(#panelShade)"/>
      <path d="M0 208 H38 Q50 208 52 196 L54 168 Q56 156 68 156 H360 Q372 156 374 168 L376 184 Q378 196 390 196 H630" fill="none" stroke="var(--accent-blue)" stroke-width="3"/>
    </svg>
    <div class="logo">Rivo<br>Tanza</div>
    <h1 class="owner-name">Darren PULKETT</h1>
    <p class="owner-title">Qualified and Passionate Motorcycle Technician</p>
    <dl class="contact-list">
      <dt class="contact-label">Phone</dt><dd class="contact-value">0471 582 930</dd>
      <dt class="contact-label">Email</dt><dd class="contact-value">rivotanza@quillmail.example</dd>
      <dt class="contact-label">Address</dt><dd class="contact-value">17 Bellbrook Lane, Larkvale, QLD</dd>
      <dt class="contact-label">ABN</dt><dd class="contact-value">61 804 392 117</dd>
    </dl>
  </section>

  <section class="card card-back" aria-label="Business card back">
    <svg class="card-panel" viewBox="0 0 630 350" aria-hidden="true">
      <defs>
        <linearGradient id="panelShadeBack" x1="0" y1="0" x2="0.4" y2="1">
          <stop offset="0" stop-color="#434345"/>
          <stop offset="1" stop-color="#2b2b2d"/>
        </linearGradient>
      </defs>
      <path d="M0 190 H38 Q50 190 52 178 L54 150 Q56 138 68 138 H630 V350 H0 Z" fill="url(#panelShadeBack)"/>
      <path d="M0 190 H38 Q50 190 52 178 L54 150 Q56 138 68 138 H630" fill="none" stroke="var(--accent-blue)" stroke-width="3"/>
    </svg>
    <div class="logo">Rivo<br>Tanza</div>
    <ul class="service-list">
      <li class="service-item"><svg class="bullet" viewBox="0 0 12 10" aria-hidden="true"><path d="M0 0 H12 L6 10 Z" fill="var(--accent-blue)"/></svg>Servicing</li>
      <li class="service-item"><svg class="bullet" viewBox="0 0 12 10" aria-hidden="true"><path d="M0 0 H12 L6 10 Z" fill="var(--accent-blue)"/></svg>Repairs</li>
      <li class="service-item"><svg class="bullet" viewBox="0 0 12 10" aria-hidden="true"><path d="M0 0 H12 L6 10 Z" fill="var(--accent-blue)"/></svg>All makes/models</li>
      <li class="service-item"><svg class="bullet" viewBox="0 0 12 10" aria-hidden="true"><path d="M0 0 H12 L6 10 Z" fill="var(--accent-blue)"/></svg>Weekends by appt.</li>
      <li class="service-item"><svg class="bullet" viewBox="0 0 12 10" aria-hidden="true"><path d="M0 0 H12 L6 10 Z" fill="var(--accent-blue)"/></svg>Pick-up/delivery available</li>
    </ul>
  </section>

</main>
</body>
</html>
```